International Clinical Software Company needs a new business card design

We are looking for a new business card design for our company that has recently expanded into the UK market, making us a multinational company.
After having rebranded our website and produced a new style guide, we are looking for a business card that is creative and attention grabbing, while being consistent with the style and colour scheme used on the new website, www.pennick.care
We produce care management technology for the aged care market, but the main aspect we aim to communicate is the human element of our software, and the way it assists in providing better care for aged people, and stronger relationships between aged people and the staff that care for them.
Our current business card is a dark green with gold text, which makes the text quite difficult to read, not very aesthetically appealing and the colour scheme looks quite dated.
We would like something fresh and modern, that can still be colourful but doesn't use large blocks of dark colour, and uses the colours within our logo.
Something tying in with the leaves that are used in our logo could work quite nicely, along with the Autumn/Fall colours of soft greens, yellows and reds (also in our existing logo). However also happy to look at fresh, completely out of the box ideas we may not have yet considered.
Target Market(s)
The people that receive this business card work in the aged card or health industry and are either corporate/management level staff or clinical (Registered Nurses, care workers etc.)
Industry/Entity Type
Health Product
Contact Information for Business Card
Company Name - PennickCare
Company locations: United Kingdom, Australia, New Zealand
Staff Details:
Staff name: Dermot Marlow
Staff job title: Executive Chairman
Staff email: d.marlow@pennick.care
Office phone number: 01632 960481
Other font styles liked:
- Calibri
Requirements
Must have
- Must include the PennickCare brand name in it's current font
- Must include logo (3 leaves in gold circle)
- Must include Business Card Details
Nice to have
- Elements of gold
- White space
- Something autumn themed but not too cliched
Should not have
- No blue - used by a major competitor and we would like to differentiate from them
- Large blocks of dark green colour (the green that appears in our leaves on the logo on our current business card is the background colour and it is far too dark)

```html
<!DOCTYPE html>
<html lang="en">
<head>
<meta charset="utf-8">
<title>PennickCare Business Card</title>
<link href="https://fonts.googleapis.com/css2?family=Open+Sans:wght@300;400;600&display=swap" rel="stylesheet">
<style>
  :root {
    --backdrop: #ece8e1;
    --card-white: #ffffff;
    --gold: #b29d70;
    --gold-text: #a8956a;
    --crimson: #a01c3a;
    --olive: #6f6a2c;
    --muted: #8a7a55;
  }
  * { box-sizing: border-box; margin: 0; padding: 0; }
  html, body {
    width: 1200px; height: 1000px; overflow: hidden;
    background: var(--backdrop);
    font-family: "Open Sans", Arial, sans-serif;
  }
  .canvas { position: relative; width: 1200px; height: 1000px; }
  .card {
    position: absolute; left: 265px; width: 665px; height: 397px;
    border-radius: 22px; overflow: hidden;
    box-shadow: 0 4px 14px rgba(0,0,0,0.18);
  }
  .card--front { top: 73px; background: var(--card-white); }
  .card--back { top: 533px; background: var(--gold); }

  .brand-mark {
    position: absolute; left: 50%; transform: translateX(-50%);
    border-radius: 50%; border-style: solid;
  }
  .card--front .brand-mark { top: 49px; width: 88px; height: 88px; border-width: 3px; border-color: var(--gold); }
  .card--back .brand-mark { top: 81px; width: 138px; height: 138px; border-width: 4px; border-color: var(--card-white); left: 342px; }

  .brand-name {
    position: absolute; left: 0; right: 0; text-align: center;
    font-weight: 300; letter-spacing: 1px;
  }
  .card--front .brand-name { top: 140px; font-size: 60px; color: var(--gold-text); left: 0; right: 0; }
  .card--back .brand-name { top: 235px; font-size: 76px; color: var(--card-white); left: 20px; }

  .staff-name {
    position: absolute; top: 258px; left: 0; right: 0; text-align: center;
    font-size: 21px; font-weight: 600; color: var(--crimson); letter-spacing: 0.5px;
  }
  .staff-title {
    position: absolute; top: 287px; left: 0; right: 0; text-align: center;
    font-size: 15px; color: var(--muted);
  }
  .contact-row {
    position: absolute; top: 324px; left: 0; right: 0;
    display: flex; justify-content: center; align-items: center; gap: 22px;
    font-size: 15px; color: var(--muted);
  }
  .contact-item { display: flex; align-items: center; gap: 8px; }
  .contact-item--phone { letter-spacing: 2.5px; }
  .contact-icon { width: 22px; height: 22px; }
  .locations-band {
    position: absolute; left: 0; right: 0; bottom: 0; height: 33px;
    background: var(--gold); color: var(--card-white);
    display: flex; align-items: center; justify-content: center;
    font-size: 15px; letter-spacing: 2px;
  }
</style>
</head>
<body>
<div class="canvas">
  <section class="card card--front">
    <div class="brand-mark"></div>
    <div class="brand-name">PennickCare</div>
    <div class="staff-name">DERMOT MARLOW</div>
    <div class="staff-title">Executive Chairman</div>
    <div class="contact-row">
      <span class="contact-item contact-item--phone">01632 960481
        <svg class="contact-icon" viewBox="0 0 22 22" aria-hidden="true">
          <circle cx="11" cy="11" r="9.5" fill="none" stroke="var(--olive)" stroke-width="1.5"/>
          <path d="M7.5 6.5c.6-.6 1.4-.5 1.8.1l.9 1.4c.3.5.2 1.1-.2 1.5l-.6.5c.6 1.3 1.5 2.2 2.8 2.8l.5-.6c.4-.4 1-.5 1.5-.2l1.4.9c.6.4.7 1.2.1 1.8l-.6.6c-.8.8-2 .8-3 .3-2.2-1.1-3.9-2.8-5-5-.5-1-.5-2.2.3-3z" fill="var(--olive)"/>
        </svg>
      </span>
      <span class="contact-item">
        <svg class="contact-icon" viewBox="0 0 22 22" aria-hidden="true">
          <circle cx="11" cy="11" r="9.5" fill="none" stroke="var(--olive)" stroke-width="1.5"/>
          <rect x="6" y="7.5" width="10" height="7" fill="var(--olive)"/>
          <path d="M6 7.5l5 4 5-4" fill="none" stroke="#fff" stroke-width="1"/>
        </svg>
        d.marlow@pennick.care
      </span>
    </div>
    <div class="locations-band">United Kingdom, Australia, New Zealand</div>
  </section>

  <section class="card card--back">
    <div class="brand-mark"></div>
    <div class="brand-name">PennickCare</div>
  </section>
</div>
</body>
</html>
```